Affinity Card (Brochure for a Fuel Card )

We need a brochure developed for a Fuel Card our company is offering to the market. Our offer has many different elements to it and as well as the benefits of the card it has geographical spread across Australia where the card is taken and where we can offer lucrative deals . The design should show the benefits of our card and also the fact it has the ability to be used Nationally as well as locally. The final design should communicate that the card is linked to both Harrowgate and Corvane (cant use the corvane logo)
The design should have a section for the applicant to put his name and address , l have supplied an example from America but want it different
It can have up to 4 folds no issues
Below are ideas for use

Target Market(s)

Fuel Card Users in all segments

Industry/Entity Type

It Company

Requirements
Must have
• Be able to capture attention and be handed out
• We now need the use of the Corvane sites in the brochure and drop the truck top image
• Sorry about the changes

```html
<!DOCTYPE html>
<html lang="en">
<head>
<meta charset="utf-8">
<title>Fuel Card Brochure – Inside Panel</title>
<link href="https://fonts.googleapis.com/css2?family=Jost:wght@400;500;700;800&display=swap" rel="stylesheet">
<style>
  :root {
    --brand-red: #ed1c2e;
    --ink: #2b2b2b;
    --paper: #ffffff;
    --backdrop: #e9e6e1;
    --map-land: #ece8dc;
    --map-water: #a9c7e8;
  }
  * { box-sizing: border-box; margin: 0; padding: 0; }
  html, body { width: 1200px; height: 1200px; overflow: hidden; }
  body {
    background: var(--backdrop);
    font-family: "Jost", "Futura", sans-serif;
    color: var(--ink);
  }
  .page {
    position: absolute;
    left: 190px; top: 20px;
    width: 820px; height: 1160px;
    background: var(--paper);
    box-shadow: 0 4px 14px rgba(0,0,0,.18);
  }
  .column { position: absolute; top: 46px; }
  .column--left { left: 23px; width: 390px; }
  .column--right { left: 433px; width: 370px; }

  .section { margin-bottom: 18px; }
  .section__title {
    color: var(--brand-red);
    font-weight: 800;
    font-size: 22px;
    line-height: 24px;
    text-transform: uppercase;
    letter-spacing: .2px;
  }
  .section__title--mixed { text-transform: none; line-height: 24px; }
  .section__intro { font-size: 15.5px; line-height: 18px; }
  .benefits { list-style: none; }
  .benefits li {
    position: relative;
    padding-left: 20px;
    font-size: 15.5px;
    line-height: 18.2px;
  }
  .benefits li::before {
    content: "•";
    position: absolute; left: 2px; top: 0;
    font-size: 12px;
  }
  .benefits strong { font-weight: 700; }

  .hours-panel {
    position: absolute;
    left: 433px; top: 621px;
    width: 363px; height: 132px;
    background: var(--brand-red);
    color: #fff;
    text-align: center;
    padding-top: 10px;
  }
  .hours-panel__title { font-weight: 800; font-size: 44px; line-height: 46px; }
  .hours-panel__text { font-size: 28px; line-height: 29px; font-weight: 400; }

  .locations-map {
    position: absolute;
    left: 23px; top: 795px;
    width: 773px; height: 340px;
    background: linear-gradient(160deg, var(--map-land) 0%, var(--map-land) 55%, var(--map-water) 85%);
  }
</style>
</head>
<body>
  <main class="page">
    <div class="column column--left">
      <section class="section">
        <h2 class="section__title">Convenience</h2>
        <ul class="benefits">
          <li>24/7 local Diesel truck refuelling outlets</li>
          <li>Ad blue available at the bowser</li>
          <li>B Double &amp; Road train access</li>
          <li>Heavy vehicle approved routes</li>
          <li>Expanding network</li>
          <li>Access to Corvane and Marlow network across Australia</li>
        </ul>
      </section>
      <section class="section">
        <h2 class="section__title">Cost Benefit</h2>
        <ul class="benefits">
          <li>Up to 6 cents per litre off at the below Harrowgate/Corvane sites: (insert small map of aus highlighting)</li>
          <li>Up to 4 cents per litre off across the corvane Australia network</li>
          <li>Always competitive board prices</li>
          <li>Reduce fraud risk</li>
        </ul>
      </section>
      <section class="section">
        <h2 class="section__title">Manage Your Account Online</h2>
        <ul class="benefits">
          <li>Download Statements</li>
          <li>Concise fleet reporting</li>
          <li>Automatic reporting</li>
          <li>Odometer audits</li>
          <li>Transaction extracts</li>
          <li>Cost centre summary</li>
          <li>Litres per 100km</li>
          <li>Active card listings</li>
          <li>Expiring fuel cards</li>
          <li>Exception reports</li>
        </ul>
      </section>
      <section class="section">
        <h2 class="section__title">Customised Card Management</h2>
        <ul class="benefits">
          <li>Card management – order, delete, suspend and alter cards. Manage cost centres &amp; set pins</li>
          <li>Shop sales option</li>
          <li>Truck wash option</li>
        </ul>
      </section>
    </div>

    <div class="column column--right">
      <section class="section">
        <h2 class="section__title">Security</h2>
        <p class="section__intro">We recognise that card security is a priority for all customers</p>
        <ul class="benefits">
          <li><strong>Personal Identification Number (PIN)</strong> - the preferred security measure, PINs can be used for vehicle specific cards and for those cardholders who prefer a PIN instead of a signature</li>
          <li><strong>Signature</strong> - used in cases where the card will only be used by an individual cardholder.</li>
          <li><strong>Odometer readings</strong> - when selected, cardholders will be prompted to supply odometer readings to the console operator at time of purchase. The use of odometer readings provides additional tracking measures for the organisation.</li>
          <li><strong>Purchase limits</strong> - can also be nominated on individual cards and will restrict purchases by time, volume or dollars</li>
        </ul>
      </section>
      <section class="section">
        <h2 class="section__title section__title--mixed">Control /Flexibility/ Simplicity and Convenience the cornerstone of our card offer</h2>
        <ul class="benefits">
          <li>We let and enable you to control your cards and your business in the simplest possible way</li>
          <li>Payment terms up to 50 days from transaction</li>
        </ul>
      </section>
    </div>

    <div class="hours-panel">
      <p class="hours-panel__title">24 HOURS</p>
      <p class="hours-panel__text">Truck Locations we have developed for you</p>
    </div>

    <div class="locations-map" role="img" aria-label="Street map of the western suburbs and bay area showing the truck refuelling site marked with a pin"></div>
  </main>
</body>
</html>
```